Simple elegant business card

General card for a fin and television director.
Just want name, email, phone and address.

Target Market(s)

Prospective employers

Industry/Entity Type

Business

Requirements
Must have
• As above
Nice to have
• Logo but not necessary.
Should not have
• Not too colourful or funky.
• Simplicity and elegance the way to go.

```html
<!DOCTYPE html>
<html lang="en">
<head>
<meta charset="utf-8">
<title>Lena Marsh – Director</title>
<link href="https://fonts.googleapis.com/css2?family=Tulpen+One&display=swap" rel="stylesheet">
<style>
  :root {
    --page: #ffffff;
    --card: #000000;
    --slate-blue: #27aae1;
    --ink: #000000;
    --contact-grey: #8a939b;
  }
  html, body {
    margin: 0;
    padding: 0;
    width: 686px;
    height: 1200px;
    overflow: hidden;
    background: var(--page);
  }
  .card {
    position: relative;
    width: 686px;
    height: 1200px;
    background: var(--card);
    border-radius: 32px;
    overflow: hidden;
  }
  .slate-mark {
    position: absolute;
    left: 99px;
    top: 437px;
    width: 487px;
    height: 298px;
  }
  .slate-mark svg {
    display: block;
  }
  .director-name {
    position: absolute;
    left: 99px;
    top: 540px;
    width: 487px;
    margin: 0;
    text-align: center;
    font-family: "Tulpen One", sans-serif;
    font-weight: 400;
    font-size: 104px;
    line-height: 1;
    letter-spacing: 5px;
    color: var(--ink);
    text-transform: uppercase;
  }
  .contact {
    position: absolute;
    right: 100px;
    top: 994px;
    margin: 0;
    text-align: right;
    font-family: "Tulpen One", sans-serif;
    font-size: 46px;
    line-height: 52px;
    letter-spacing: 1px;
    color: var(--contact-grey);
    font-style: normal;
  }
  .contact span {
    display: block;
  }
</style>
</head>
<body>
  <div class="card">
    <div class="slate-mark">
      <svg width="487" height="298" viewBox="0 0 487 298" role="img" aria-label="Film clapperboard emblem in bright blue">
        <rect x="0" y="0" width="487" height="298" rx="12" fill="var(--slate-blue)"/>
        <rect x="0" y="0" width="487" height="12" fill="var(--slate-blue)"/>
      </svg>
    </div>
    <h1 class="director-name">Lena Marsh</h1>
    <address class="contact">
      <span class="contact-email">lenamarsh@mail.com</span>
      <span class="contact-phone">+1 310 555 0148</span>
    </address>
  </div>
</body>
</html>
```